Label - Australian Extra Virgin Olive Oil

I'm seeking a front and back label to apply to bottles/tins of my olive oil. They will be applied to green bottles of various sizes and also white tins. The labels will have the dimensions 70 x 120mm and printed at 600dpi on adhesive labels with metalised backing. With this material, any area which is not colored on the label will show through as silver - the design may make use of this feature. There are some obligatory labeling requirements in Australia including a logo showing the proportion of Australian content, and an indication of the harvest date - the design will need to make allowance for this. Also, since the label will be used in subsequent years and on various sizes of product, I need to be able to alter this with each print run.I have a logo to use on the front label and another I would like to use on the back as this latter one will tie in with other future products (non olive oil).
The text for the back label
"Tallowby Creek is a family run enterprise. Our olives are grown on the banks of the Wendrake River in Central Victoria and processed locally
email; quietheron@pelinet.com.au
text needed for the front label design
"Australian Extra-Virgin Olive Oil"

```html
<!DOCTYPE html>
<html lang="en">
<head>
<meta charset="utf-8">
<title>Tallowby Creek – Olive Oil Labels</title>
<link rel="stylesheet" href="https://fonts.googleapis.com/css2?family=Cabin:wght@400;500&family=Archivo+Black&display=swap">
<style>
  :root {
    --page: #ffffff;
    --green-deep: #1f4a0c;
    --green-mid: #2f6414;
    --green-light: #5b8a2a;
    --ink-white: #ffffff;
    --ink-green: #2c5a12;
    --ink-black: #0a0a0a;
  }
  * { box-sizing: border-box; margin: 0; padding: 0; }
  html, body { width: 933px; height: 1200px; overflow: hidden; background: var(--page); }
  .sheet {
    position: relative; width: 933px; height: 1200px;
    font-family: "Cabin", sans-serif;
  }
  .panel { position: absolute; top: 235px; width: 380px; }
  .panel--front { left: 58px; }
  .panel--back { left: 495px; }
  .label {
    position: relative; width: 380px; height: 630px; overflow: hidden;
    color: var(--ink-white); text-align: center;
  }
  .label--front {
    background:
      radial-gradient(ellipse 60% 30% at 60% 48%, rgba(120,170,70,0.35), transparent 70%),
      radial-gradient(ellipse 80% 40% at 30% 75%, rgba(90,140,50,0.35), transparent 70%),
      linear-gradient(175deg, var(--green-light) 0%, var(--green-mid) 25%, var(--green-deep) 55%, var(--green-mid) 85%, var(--green-light) 100%);
  }
  .label--back {
    background:
      radial-gradient(ellipse 50% 20% at 75% 2%, rgba(140,190,90,0.4), transparent 70%),
      linear-gradient(180deg, var(--green-deep) 0%, var(--green-mid) 45%, var(--green-light) 100%);
  }
  .brand-name {
    position: absolute; left: 0; right: 0;
    font-family: "Cabin", sans-serif; font-weight: 500; color: var(--ink-white);
  }
  .label--front .brand-name { top: 165px; font-size: 32px; }
  .label--back .brand-name { top: 150px; font-size: 30px; letter-spacing: 1px; }
  .product-title { position: absolute; top: 270px; left: 0; right: 0; font-weight: 400; line-height: 1; }
  .product-title .origin { display: block; font-size: 52px; }
  .product-title .grade { display: block; font-size: 32px; margin-top: 8px; }
  .product-title .kind { display: block; font-size: 49px; margin-top: 12px; }
  .volume {
    position: absolute; top: 492px; left: 50%; transform: translateX(-50%);
    width: 134px; height: 38px; background: var(--ink-white); color: var(--ink-green);
    font-size: 20px; line-height: 38px;
  }
  .story {
    position: absolute; top: 283px; left: 20px; right: 20px;
    font-size: 15.5px; line-height: 19px;
  }
  .origin-badge {
    position: absolute; top: 446px; left: 44px; width: 79px; height: 113px;
    background: var(--ink-white); border: 2px solid #1a8a6a; border-radius: 3px;
  }
  .harvest-date {
    position: absolute; top: 478px; left: 141px; width: 181px; height: 59px;
    background: var(--ink-white); color: var(--ink-green);
    font-size: 13.5px; line-height: 17px; padding-top: 12px;
  }
  .caption {
    margin-top: 38px; text-align: center;
    font-family: "Archivo Black", sans-serif; font-size: 52px; color: var(--ink-black);
    letter-spacing: 1px;
  }
</style>
</head>
<body>
<main class="sheet">
  <section class="panel panel--front">
    <div class="label label--front">
      <div class="brand-name">Tallowby Creek</div>
      <h1 class="product-title">
        <span class="origin">Australian</span>
        <span class="grade">Extra-Virgin</span>
        <span class="kind">Olive Oil</span>
      </h1>
      <div class="volume">Vol : 750 Ml</div>
    </div>
    <p class="caption">FRONT</p>
  </section>

  <section class="panel panel--back">
    <div class="label label--back">
      <div class="brand-name">TALLOWBY CREEK</div>
      <p class="story">"Tallowby Creek is a family run enterprise.<br>
        Our olives are grown on the banks of the<br>
        Wendrake River in Central Victoria<br>
        and processed locally<br>
        Email: quietheron@pelinet.com.au</p>
      <div class="origin-badge" role="img" aria-label="Country of origin content badge"></div>
      <div class="harvest-date">Harvest Date room to<br>handwrite date</div>
    </div>
    <p class="caption">BACK</p>
  </section>
</main>
</body>
</html>
```